Velvet Crypt Mixtape Podcast Design

My audio drama podcast is a funny horror story with romantic elements called Velvet Crypt Mixtape.
I'm looking for a colorful design featuring the title and letting the viewer know this is a horror show.
The title needs to be clearly visible even in thumbnail size.

```html
<!DOCTYPE html>
<html lang="en">
<head>
<meta charset="utf-8">
<title>Velvet Crypt Mixtape</title>
<link rel="stylesheet" href="https://fonts.googleapis.com/css2?family=Creepster&display=swap">
<style>
  :root {
    --maroon: #4a0e0c;
    --rust: #8f2f0c;
    --orange: #c9580f;
    --amber: #de7a25;
    --night: #120a2e;
    --title: #ffffff;
    --ghost-light: #fbf9fb;
    --ghost-shade: #e4dbe3;
    --ghost-violet: #55209a;
  }
  html, body {
    margin: 0;
    padding: 0;
    overflow: hidden;
    background: var(--night);
  }
  .cover {
    position: relative;
    width: 1200px;
    height: 1200px;
    overflow: hidden;
    background:
      radial-gradient(ellipse 520px 420px at 560px 330px, rgba(222,122,37,0.85), rgba(222,122,37,0) 70%),
      radial-gradient(ellipse 620px 520px at 360px 820px, rgba(201,88,15,0.9), rgba(201,88,15,0) 70%),
      radial-gradient(ellipse 560px 460px at 80px 120px, rgba(74,14,12,0.95), rgba(74,14,12,0) 75%),
      radial-gradient(ellipse 640px 640px at 1180px 1160px, var(--night), rgba(18,10,46,0) 75%),
      linear-gradient(135deg, var(--maroon) 0%, var(--rust) 22%, var(--orange) 45%, var(--amber) 55%, var(--orange) 64%, #3a1420 80%, var(--night) 100%);
  }
  .title {
    position: absolute;
    inset: 0;
    margin: 0;
    display: flex;
    flex-direction: column;
    align-items: center;
    justify-content: center;
    font-family: "Creepster", "Impact", sans-serif;
    font-weight: 400;
    color: var(--title);
    line-height: 0.92;
    text-transform: uppercase;
  }
  .title__line {
    display: flex;
    align-items: flex-end;
    justify-content: center;
    white-space: nowrap;
  }
  .title__line--top { font-size: 190px; letter-spacing: 4px; gap: 18px; }
  .title__line--middle { font-size: 236px; letter-spacing: 8px; }
  .title__line--bottom { font-size: 196px; letter-spacing: 4px; }
  .ghost {
    width: 130px;
    height: 250px;
    margin-bottom: 10px;
    border-radius: 65px 65px 30px 10px;
    background:
      linear-gradient(160deg, var(--ghost-light) 0%, var(--ghost-shade) 70%, var(--ghost-violet) 100%);
  }
</style>
</head>
<body>
  <main class="cover">
    <h1 class="title">
      <span class="title__line title__line--top">
        <span>Velvet</span>
        <span class="ghost" role="img" aria-label="Illustration of a frightened white ghost with a purple hem"></span>
      </span>
      <span class="title__line title__line--middle">Crypt</span>
      <span class="title__line title__line--bottom">Mixtape</span>
    </h1>
  </main>
</body>
</html>
```